I need a letterhead for a newsletter that will go out quarterly to the dentists of the 18th district. It is called "The Cobalt Bulletin" We are in Amarillo TX and have this landmark in the photo as our most prominent feature. If it could be used, that would be cool.
This is a professional organization newsletter so the letterhead should be somewhat professional.

Target Market(s)

Dentists

Industry/Entity Type

Dental

Font styles to use
Serif

Colors

Designer to choose only greyscale colors for use in the design.

Requirements
Must have
• I want the title of "The Cobalt Bulletin" to be the on top with the phrase "Brookmere Valley Dental Guild" written underneath.
Nice to have
• the photo incorporated could be incorporated in black and white or color along the bottom of the letterhead or with the title inside the photo.
Should not have
• I don't want it to be cartoony. I want it to be stylish and elegant and professional.

```html
<!DOCTYPE html>
<html lang="en">
<head>
<meta charset="utf-8">
<title>The Cobalt Bulletin – Letterhead</title>
<link href="https://fonts.googleapis.com/css2?family=Bebas+Neue&family=Lato:wght@400;700&family=Open+Sans:wght@400;600&display=swap" rel="stylesheet">
<style>
  :root {
    --paper: #ffffff;
    --ink: #1c1c1c;
    --body-ink: #4a4a4a;
    --band: #d9d8da;
    --photo-sky: #c9d3de;
    --photo-ground: #b7a89a;
  }
  * { margin: 0; padding: 0; box-sizing: border-box; }
  html, body { width: 1040px; height: 1200px; overflow: hidden; background: var(--paper); }
  .letterhead { position: relative; width: 1040px; height: 1200px; background: var(--paper); color: var(--body-ink); font-family: "Open Sans", sans-serif; }

  .masthead { position: absolute; top: 30px; left: 0; width: 100%; text-align: center; color: var(--ink); }
  .masthead-title { font-family: "Bebas Neue", sans-serif; font-weight: 400; font-size: 54px; line-height: 1; letter-spacing: 0.5px; }
  .masthead-subtitle { font-family: "Lato", sans-serif; font-size: 19px; letter-spacing: 0.4px; text-transform: uppercase; margin-top: 2px; }

  .letter { position: absolute; left: 97px; width: 840px; font-size: 16px; line-height: 27px; }
  .issue-date { top: 245px; }
  .recipient { top: 285px; line-height: 19px; }
  .salutation { top: 382px; }
  .letter-body { top: 437px; }
  .letter-body p { text-align: justify; hyphens: auto; margin-bottom: 27px; }
  .closing { top: 843px; }
  .signatory { top: 918px; }
  .signatory-name { font-size: 20px; font-weight: 600; color: #333; line-height: 28px; }
  .signatory-role { font-size: 16px; line-height: 24px; }

  .footer-art { position: absolute; left: 0; top: 1020px; width: 1040px; height: 180px; }
  .contact { position: absolute; left: 96px; top: 1103px; font-family: "Lato", sans-serif; font-style: normal; font-size: 19px; color: var(--ink); line-height: 25px; }
  .contact strong { font-weight: 700; }
  .contact-address { margin-top: 8px; }
</style>
</head>
<body>
<main class="letterhead">
  <header class="masthead">
    <h1 class="masthead-title">The Cobalt Bulletin</h1>
    <p class="masthead-subtitle">Brookmere Valley Dental Guild</p>
  </header>

  <p class="letter issue-date">Issuing Date: May 5, 2018</p>
  <p class="letter recipient">Name Of Employee Mr. Dalton Reyes<br>Address of Employee<br>Address Line 2 etc..</p>
  <p class="letter salutation">Dear Mr. Dalton Reyes</p>

  <section class="letter letter-body">
    <p>Lorem Ipsum has been the industry's standard dummy text ever since the 1500s, when an unknown printer took a galley of type and scrambled it to make a type specimen book. It has survived not only five centuries, but also the leap into electronic typesetting, remaining essentially unchanged. It was popularised in the 1960s with the release of Tessaline sheets containing Lorem Ipsum passages, and more recently with desktop publishing software like Quillset Composer including versions of Lorem Ipsum.</p>
    <p>Lorem Ipsum is simply dummy text of the printing and typesetting industry. Lorem Ipsum has been the industry's standard dummy text ever since the 1500s, when an unknown printer took a galley of type and scrambled it to make a type specimen book.</p>
    <p>It has survived not only five centuries, but also the leap into electronic typesetting, remaining essentially unchanged. It was popularised in the 1960s with the release of Tessaline sheets containing Lorem IpsumIpsum passages.</p>
  </section>

  <p class="letter closing">Yours Sincerely</p>
  <div class="letter signatory">
    <p class="signatory-name">Marcus Ellery</p>
    <p class="signatory-role">Managing Director</p>
  </div>

  <svg class="footer-art" viewBox="0 0 1040 180">
    <defs>
      <linearGradient id="landmarkTones" x1="0" y1="0" x2="0" y2="1">
        <stop offset="0" stop-color="#c9d3de"/>
        <stop offset="0.6" stop-color="#d4c3b8"/>
        <stop offset="1" stop-color="#b7a89a"/>
      </linearGradient>
    </defs>
    <polygon points="0,75 545,75 508,180 0,180" fill="#d9d8da"/>
    <polygon points="576,0 1027,0 1027,180 545,180" fill="url(#landmarkTones)" opacity="0.85" role="img" aria-label="Photograph of the canyon lighthouse rock formation under a pale sky"/>
  </svg>

  <address class="contact">
    <div><strong>P:</strong> 055-310 772 418 | <strong>E:</strong> hello@cobaltbulletin.org</div>
    <div><strong>www.cobaltbulletin.org</strong></div>
    <div class="contact-address">87, Mesa Ridge Road,&nbsp; 79104 United States</div>
  </address>
</main>
</body>
</html>
```